Lantern Square, Steady Course. (Website Design)

We are launching a new bipartisan civic movement: Lantern Square. Steady Course.
The mission is this: Americans deserve a government that is legally required to serve them honestly.
We are looking for a world-class website designer capable of creating an emotionally powerful, modern, cinematic landing page experience that feels larger than politics.
This is not a campaign website for a political party or candidate. We are not looking for a red, white, and blue page with stripes, or American flags, or stock footage of smiling people in a voting booth. We are looking for an emotional and cinematic experience through and through.
The visual direction should feel:
Historic
Hopeful
American
Emotional
Cinematic
Trustworthy
Timeless
The goal is to make visitors feel that they are witnessing the beginning of something important and want to be part of it in the end.
Primary Objective:
Inspire visitors to participate in a one-minute survey and cast their vote.
The survey itself is extremely short and takes approximately one minute to complete.
Everything on the page should ultimately guide visitors toward this action while creating enough curiosity, trust, emotional engagement, and excitement that they feel compelled to take part in the movement.
Audience:
The audience is ordinary Americans across the political spectrum: Democrats, Republicans, Independents.
The design should feel unifying and welcoming.
It should avoid looking partisan, ideological, activist, or government-issued.
Creative Freedom:
We are intentionally giving designers substantial creative freedom.
We are not looking for someone to simply arrange content into predefined sections.
Instead, we are looking for a designer who can think strategically about user experience and persuasion.
The ideal design is as minimal as possible, but you may always:
Use as many sections as you believe are necessary.
Use as many images as you believe are necessary.
Include storytelling elements.
Include data visualizations.
Include timelines.
Include videos.
Include animations.
Include or exclude sections as you see fit.
Reorganize the flow entirely.
We uploaded some files containing text and section suggestions. You don’t have to use them.
We also uploaded some images to convey the general feel we’re looking for.
We are much more interested in the effectiveness of the overall experience than in any specific layout.
What success looks like:
Think outside the box.
Please do not create another generic political website. We have already explored those approaches.
We are looking for something different.
The winning design will be the one that most effectively guides visitors from curiosity to belief to participation.
When a visitor reaches the end of the experience, they should feel:
This is bigger than politics.
This is something I can support regardless of party.
This feels credible.
This feels hopeful.
I want to be part of this.
Use the survey results, the research findings, the principles, the storytelling, or any other elements you believe will help build trust and inspire participation.
Don't just impress us with flashy visuals. Impress us with a website experience that inspires people to become part of the movement and cast their vote.
The final call-to-action should feel like the natural conclusion of the journey, not a request for engagement.
Our goal is not simply to inform visitors. Our goal is to inspire them to cast their vote.
Prioritize emotional impact, storytelling, clarity, and persuasion over decorative design elements.
Final words:
Design a website experience that successfully inspires visitors to take the survey and cast their vote.
Think like a storyteller, not just a designer.
Thank you for your interest in the project.
Best of luck.

```html
<!DOCTYPE html>
<html lang="en">
<head>
<meta charset="utf-8">
<title>Lantern Square. Steady Course. — Landing Page</title>
<link href="https://fonts.googleapis.com/css2?family=Playfair+Display:wght@400;500&family=Poppins:wght@400;500;600&display=swap" rel="stylesheet">
<style>
:root{
  --board:#c9a06b;
  --navy:#0b1424;
  --gold:#c9a06b;
  --ink:#1a1f2b;
  --muted:#6b6f78;
  --white:#ffffff;
  --hero-top:#4a5570;
  --hero-bottom:#1a2336;
}
*{margin:0;padding:0;box-sizing:border-box}
html,body{width:874px;height:1200px;overflow:hidden;background:var(--board)}
.board{position:absolute;left:0;top:0;width:1651px;height:2268px;transform:scale(.5294);transform-origin:0 0;background:var(--board);font-family:'Poppins',sans-serif;color:var(--ink)}
.abs{position:absolute}
.serif{font-family:'Playfair Display',serif;font-weight:400}
.gold{color:var(--gold)}
.white{color:var(--white)}
.label{font-size:10px;letter-spacing:.3px;color:var(--gold);text-transform:uppercase}
.small{font-size:8px;line-height:14px}
.h2{font-size:24px;line-height:29px}
.center{text-align:center;transform:translateX(-50%)}
.btn{display:flex;align-items:center;justify-content:center;font-size:8px;font-weight:600;text-transform:uppercase;letter-spacing:.2px}
.page{position:absolute;background:var(--white);overflow:hidden}
.left{left:84px;top:70px;width:708px;height:2198px}
.right{left:856px;top:0;width:708px;height:1723px}
.band{position:absolute;left:0;width:708px}
.logo{font-size:14px;line-height:22px}
.vline{position:absolute;width:1px;background:#8a8f99}
</style>
</head>
<body>
<div class="board">

  <!-- LEFT COLUMN -->
  <section class="page left">
    <!-- Hero -->
    <div class="band" style="top:0;height:527px;background:linear-gradient(180deg,var(--hero-top),var(--hero-bottom))" role="img" aria-label="Cinematic photo of a lone hiker standing on a mountain ridge above misty valleys"></div>
    <div class="abs serif logo white" style="left:86px;top:22px">Lantern Square.<br><span class="gold">Steady Course.</span></div>
    <div class="abs white" style="left:582px;top:26px;font-size:9px;display:flex;align-items:center;gap:4px">
      <svg width="8" height="8" viewBox="0 0 8 8"><rect width="3.5" height="3.5" fill="#fff"/><rect x="4.5" width="3.5" height="3.5" fill="#fff"/><rect y="4.5" width="3.5" height="3.5" fill="#fff"/><rect x="4.5" y="4.5" width="3.5" height="3.5" fill="#fff"/></svg>Menu
    </div>
    <svg class="abs" style="left:84px;top:156px" width="64" height="64" viewBox="0 0 64 64" aria-label="Play film">
      <circle cx="32" cy="32" r="31" fill="none" stroke="#fff" stroke-width="1"/>
      <circle cx="32" cy="32" r="25" fill="#fff" stroke="#9aa0ad" stroke-width="3"/>
      <path d="M29 27 L37 32 L29 37Z" fill="var(--navy)"/>
    </svg>
    <h1 class="abs serif white" style="left:389px;top:96px;font-size:40px;line-height:42px">Lantern<br>Square.<br><span class="gold">Steady Course.</span></h1>
    <div class="abs btn white" style="left:390px;top:243px;width:162px;height:27px;background:var(--gold)">Vote in the 1-minute survey</div>
    <p class="abs white" style="left:86px;top:372px;font-size:9.5px;line-height:16px">Americans may disagree on politics.<br>But we can agree on one thing:<br><br>Government should be legally required <span class="gold">to serve the<br>people honest!</span></p>
    <div class="vline" style="left:595px;top:353px;height:110px;background:#9aa3b5"></div>
    <div class="abs white" style="left:574px;top:479px;font-size:7px">Scroll Down</div>

    <!-- Trust gap -->
    <div class="band" style="top:527px;height:302px;background:var(--navy)"></div>
    <h2 class="abs serif h2 white" style="left:86px;top:585px">The Trust Gap</h2>
    <p class="abs small white" style="left:86px;top:630px">For decades, Americans have watched political battles dominate the headlines while confidence in public<br>institutions continues to decline.</p>
    <div class="abs" style="left:114px;top:694px"><div class="serif gold" style="font-size:15px">68%</div><p class="small white" style="margin-top:4px">Americans say government<br>is broken and needs<br>major reform.</p></div>
    <div class="abs" style="left:321px;top:694px"><div class="serif gold" style="font-size:15px">75%</div><p class="small white" style="margin-top:4px">Feel politicians are more<br>focused on power than<br>people.</p></div>
    <div class="abs" style="left:519px;top:694px"><div class="serif gold" style="font-size:15px">57%</div><p class="small white" style="margin-top:4px">Believe their voice has little<br>impact on government<br>decisions.</p></div>

    <!-- Agreement -->
    <div class="abs label" style="left:86px;top:891px">A different starting point</div>
    <h2 class="abs serif h2" style="left:86px;top:917px">What If We Started With<br>The One Thing Most Americans<br>Already Agree On?</h2>
    <p class="abs small" style="left:86px;top:1031px;color:var(--muted)">Regardless of party, most Americans want honest,<br>accountable government.</p>
    <svg class="abs" style="left:248px;top:1073px" width="202" height="202" viewBox="0 0 202 202">
      <circle cx="101" cy="101" r="94" fill="none" stroke="var(--navy)" stroke-width="13"/>
    </svg>
    <div class="abs serif" style="left:316px;top:1130px;font-size:40px">97<span style="font-size:26px">%</span></div>
    <div class="abs gold" style="left:323px;top:1185px;font-size:15px;letter-spacing:1px">AGREE</div>
    <p class="abs small" style="left:478px;top:1277px;color:var(--muted)">97% of Americans believe government<br>should be honest and transparent.</p>
    <p class="abs small" style="left:478px;top:1312px;color:var(--muted)">Common values.<br>Shared future.</p>

    <!-- Movement -->
    <div class="abs" style="left:0;top:1412px;width:353px;height:365px;background:var(--navy)"></div>
    <div class="abs" style="left:353px;top:1412px;width:355px;height:365px;background:linear-gradient(135deg,#5a6274,#262d3b)" role="img" aria-label="Black-and-white portrait of a thoughtful man seated by a weathered wall"></div>
    <div class="abs label" style="left:85px;top:1464px">A movement, not a party</div>
    <h2 class="abs serif h2 white" style="left:85px;top:1490px">This Isn't<br>A Political Party.<br>This Is A Civic<br>Standard.</h2>
    <div class="abs white" style="left:86px;top:1631px;font-size:7.5px">NOT LEFT. NOT RIGHT. FORWARD.</div>
    <p class="abs small white" style="left:86px;top:1656px">Create legally enforceable standards of honesty,<br>transparency, and accountability for those entrusted<br>to govern.</p>
    <p class="abs small white" style="left:86px;top:1712px">Because public service should answer to the public.</p>
    <svg class="abs" style="left:659px;top:1570px" width="8" height="38"><circle cx="4" cy="4" r="2.5" fill="#8a93a5"/><circle cx="4" cy="18" r="2.5" fill="#8a93a5"/><circle cx="4" cy="32" r="2.5" fill="var(--gold)"/></svg>

    <!-- Process -->
    <div class="abs label center" style="left:354px;top:1847px">How it works</div>
    <h2 class="abs serif center" style="left:354px;top:1870px;font-size:24px;white-space:nowrap">Our Simple Process</h2>
    <svg class="abs" style="left:328px;top:1944px" width="56" height="56" viewBox="0 0 56 56">
      <circle cx="26" cy="30" r="24" fill="var(--navy)"/>
      <rect x="17" y="24" width="16" height="10" fill="none" stroke="#fff" stroke-width="1.2" transform="rotate(-30 25 29)"/>
      <line x1="15" y1="37" x2="37" y2="37" stroke="#fff" stroke-width="1.2"/>
      <circle cx="42" cy="7" r="5" fill="var(--gold)"/>
    </svg>
    <div class="abs center" style="left:354px;top:2010px;font-size:10px;letter-spacing:.3px;white-space:nowrap">AMERICANS VOTE</div>
    <p class="abs small center" style="left:354px;top:2032px;color:var(--muted);white-space:nowrap;text-align:center">Citizens participate in a brief one-minute survey<br>and share their views on the principles that matter most.</p>
    <div class="vline" style="left:354px;top:2080px;height:55px"></div>
  </section>

  <!-- RIGHT COLUMN -->
  <section class="page right">
    <div class="abs label center" style="left:354px;top:51px">How it works</div>
    <h2 class="abs serif center" style="left:354px;top:74px;font-size:24px;white-space:nowrap">Our Simple Process</h2>
    <svg class="abs" style="left:328px;top:147px" width="56" height="56" viewBox="0 0 56 56">
      <circle cx="26" cy="28" r="24" fill="var(--navy)"/>
      <rect x="17" y="22" width="16" height="10" fill="none" stroke="#fff" stroke-width="1.2" transform="rotate(-30 25 27)"/>
      <line x1="15" y1="35" x2="37" y2="35" stroke="#fff" stroke-width="1.2"/>
      <circle cx="42" cy="7" r="5" fill="var(--gold)"/>
    </svg>
    <div class="abs center" style="left:354px;top:214px;font-size:10px;letter-spacing:.3px;white-space:nowrap">AMERICANS VOTE</div>
    <p class="abs small center" style="left:354px;top:236px;color:var(--muted);white-space:nowrap;text-align:center">Citizens participate in a brief one-minute survey<br>and share their views on the principles that matter most.</p>
    <div class="vline" style="left:354px;top:283px;height:60px"></div>

    <!-- Show up -->
    <div class="band" style="top:380px;height:440px;background:linear-gradient(180deg,#ffffff 0%,#ececec 55%,#e2e2e2 100%)" role="img" aria-label="Faded photo of a historic capitol dome above a city"></div>
    <div class="abs label" style="left:84px;top:460px">Why this matters</div>
    <h2 class="abs serif h2" style="left:84px;top:485px">The Future is<br>Built by People Who<br>Show Up.</h2>
    <div class="abs" style="left:287px;top:583px;width:134px;height:134px;border-radius:50%;background:#fff;display:flex;align-items:center;justify-content:center"><span class="serif" style="font-size:34px">2.4M+</span></div>
    <svg class="abs" style="left:529px;top:697px" width="66" height="24" role="img" aria-label="Small portraits of participants">
      <circle cx="12" cy="12" r="11" fill="#8c7a6a" stroke="#fff" stroke-width="1.5"/>
      <circle cx="32" cy="12" r="11" fill="#b59a80" stroke="#fff" stroke-width="1.5"/>
      <circle cx="52" cy="12" r="11" fill="#4a4d55" stroke="#fff" stroke-width="1.5"/>
    </svg>
    <p class="abs small" style="left:529px;top:734px">Americans have already<br>shared their voice.</p>

    <!-- One country -->
    <div class="abs label" style="left:84px;top:885px">Why this matters</div>
    <h2 class="abs serif h2" style="left:84px;top:911px">One Country.<br>One Voice. One Standard.</h2>
    <p class="abs small" style="left:84px;top:987px;color:var(--muted)">From small towns to big cities, Americans are coming<br>together to raise expectations and build a stronger future.</p>
    <div class="abs btn white" style="left:84px;top:1037px;width:146px;height:28px;background:var(--navy)">Explore the movement</div>
    <div class="abs" style="left:370px;top:918px;width:295px;height:154px;border-radius:10px;background:#333333" role="img" aria-label="Map of the United States showing all fifty states"></div>
    <div class="abs" style="left:95px;top:1123px;display:flex;gap:26px;font-size:8.5px;font-weight:500;align-items:center">
      <span style="display:flex;align-items:center;gap:7px"><svg width="18" height="12"><rect x="1" y="1" width="16" height="10" rx="2" fill="none" stroke="#555"/></svg>All 50 States</span>
      <span style="display:flex;align-items:center;gap:7px"><svg width="14" height="14"><circle cx="7" cy="7" r="6" fill="none" stroke="#555"/><circle cx="7" cy="6" r="2" fill="none" stroke="#555"/></svg>Thousands of Communities</span>
      <span style="display:flex;align-items:center;gap:7px"><svg width="14" height="14"><circle cx="7" cy="7" r="6" fill="none" stroke="#555"/><circle cx="7" cy="7" r="3" fill="none" stroke="#555"/></svg>One Shared Purpose</span>
    </div>

    <!-- CTA + footer -->
    <div class="band" style="top:1360px;height:363px;background:var(--navy)"></div>
    <div class="abs" style="left:85px;top:1214px;width:538px;height:292px;background:var(--gold)"></div>
    <h2 class="abs serif center white" style="left:354px;top:1258px;font-size:24px;white-space:nowrap">You Have One Minute.</h2>
    <div class="abs center white" style="left:354px;top:1303px;font-size:7px;line-height:14px;text-align:center;white-space:nowrap">
      THE FUTURE OF GOVERNMENT SHOULD NOT BELONG TO POLITICIANS ALONE.<br>IT SHOULD BELONG TO THE PEOPLE IT SERVES.<br><br>
      For generations, Americans have debated the future of our country.<br><br>
      Now, you have an opportunity to help define it. By taking a simple one-minute survey, you can help<br>identify the principles that unite Americans across political lines and shape a stronger standard for public service.<br><br>
      This is more than a survey. It's the beginning of a national conversation.
    </div>
    <div class="abs btn white" style="left:281px;top:1435px;width:146px;height:28px;background:var(--navy)">Cast your vote</div>

    <div class="abs serif logo white" style="left:84px;top:1568px">Lantern Square.<br><span class="gold">Steady Course.</span></div>
    <p class="abs white" style="left:263px;top:1569px;font-size:8px;line-height:15px">A bipartisan civic movement dedicated to establishing honest, transparent,<br>and accountable government through shared principles and citizen<br>participation.</p>
    <div class="abs white" style="left:263px;top:1626px;font-size:7.5px">Privacy Policy &nbsp;|&nbsp; Terms of Use &nbsp;|&nbsp; Accessibility Statement &nbsp;|&nbsp; Contact</div>
    <div class="abs white" style="left:263px;top:1654px;font-size:7.5px">Copyright@26.All Rights Reserved.</div>
    <div class="abs white" style="right:86px;top:1689px;font-size:7.5px">Town Hall • Porch Feed • Civic Reel • Workline</div>
  </section>

</div>
</body>
</html>
```